Corwell Holdings Business Cards

Hello. I need business cards designed with our new logo. I'd like to see at least 3 different designs. At least one with a dark background, and at least one with a white background. Maybe one with gray or blue for the background. Play with gradient colors and maybe even insert a pic of a skyline in the background of one or more of them. Use your judgement. We will need 2 cards printed. They need to accommodate the employee name, title, company address, phone, email, and website. Thanks.

Target Market(s)

Wealthy mature investors.

Contact Information for Business Card

Single-sided, professional, clean design that incorporates our logo.

Font styles to use
Sans Serif

Requirements
Must have
• Our new logo needs to be featured on it. (See attached.)
• Employee Name (In all CAPS)
• Title
• Street Address, City, ST Zip Code
• Cell Phone #, Email Address, Website Address
Nice to have
• Design that blends well with our new logo and its colors, or a city scape or other graphic design that looks like an apartment complex in the background. Blues and grays are nice, but use your judgement.
Should not have
• Modern or oriental looking designs or bright colors.

```html
<!DOCTYPE html>
<html lang="en">
<head>
<meta charset="UTF-8">
<title>Corwell Holdings – Business Card</title>
<link href="https://fonts.googleapis.com/css2?family=Montserrat:wght@400;500;700&display=swap" rel="stylesheet">
<style>
  :root {
    --paper: #ffffff;
    --brand-blue: #29a8e0;
    --ink-gray: #5a5d61;
    --rule-gray: #6b6e72;
    --band-slate: #454a51;
  }
  html, body {
    margin: 0;
    padding: 0;
    width: 1200px;
    height: 761px;
    overflow: hidden;
    background: var(--paper);
  }
  .card {
    position: relative;
    width: 1200px;
    height: 761px;
    background: var(--paper);
    font-family: "Montserrat", Arial, sans-serif;
    color: var(--ink-gray);
    overflow: hidden;
  }
  .brand {
    position: absolute;
    left: 150px;
    top: 318px;
    display: flex;
    align-items: center;
    gap: 22px;
  }
  .brand-square {
    width: 46px;
    height: 46px;
    background: var(--brand-blue);
  }
  .brand-name {
    margin: 0;
    font-size: 44px;
    font-weight: 500;
    line-height: 1.08;
    letter-spacing: 1px;
    color: var(--brand-blue);
    text-transform: uppercase;
  }
  .divider {
    position: absolute;
    left: 606px;
    width: 3px;
  }
  .divider-top { top: 202px; height: 94px; background: var(--rule-gray); }
  .divider-bottom { top: 304px; height: 248px; background: var(--brand-blue); }
  .contact {
    position: absolute;
    left: 652px;
    top: 196px;
  }
  .person-name {
    margin: 0;
    font-size: 42px;
    font-weight: 700;
    letter-spacing: 1.5px;
    color: var(--brand-blue);
    line-height: 1.1;
  }
  .person-title {
    margin: 2px 0 0;
    font-size: 28px;
    font-weight: 400;
    letter-spacing: 1px;
    line-height: 1.3;
  }
  .address, .lines {
    margin: 0;
    font-size: 27px;
    font-weight: 400;
    letter-spacing: 0.5px;
    line-height: 41px;
    font-style: normal;
  }
  .address { margin-top: 26px; }
  .lines { margin-top: 14px; padding-left: 3px; }
  .skyline {
    position: absolute;
    left: 813px;
    top: 664px;
    width: 240px;
    height: 72px;
    background: linear-gradient(to top, #454a51, #5d636b);
  }
  .base-band {
    position: absolute;
    left: 0;
    bottom: 0;
    width: 1200px;
    height: 26px;
    background: var(--band-slate);
  }
</style>
</head>
<body>
  <main class="card">
    <div class="brand">
      <div class="brand-square"></div>
      <p class="brand-name">Corwell<br>Holdings</p>
    </div>

    <div class="divider divider-top"></div>
    <div class="divider divider-bottom"></div>

    <section class="contact">
      <h1 class="person-name">DANIEL REEVE</h1>
      <p class="person-title">CEO/FOUNDER</p>
      <address class="address">4120 Alder Ridge Road<br>Juneau, Alaska 34518</address>
      <p class="lines">P : 689 555 0147<br>E: daniel@corwell.com<br>W: www.corwell.com</p>
    </section>

    <div class="skyline" role="img" aria-label="Silhouette of a city skyline with towers and a Ferris wheel"></div>
    <div class="base-band"></div>
  </main>
</body>
</html>
```